Rapidly Expanding Real Estate Firm Seeking Signage Designs for Multiple Properties

We would like a sign design template created that we can use at our apartment buildings. We would like a consistent sign appearance that is adaptable enough to be used at different locations, on different mediums, and in different sizes. All vary for signage depending on the local laws and regulations as well as the type and style of the property. But the sign design should be consistent enough to support our company's branding efforts; so people that see our sign know its our company but also that the specific property is unique. Our thought was to incorporate the property address; i.e. "418 Birch" along with a portion of our company logo(attached). Then tag our website address across the bottom. Or some combination of that structure/design. It may make sense to just use the address and website address across the bottom OR it might be good to say 418 Birch St in large font with "by Amber Ridge Holdings Group" underneath as sort of a tag line. Not quite sure.
But we definitely want the signage to be clearly visible, professional, and clean. Easily read for the street. Should be flexible enough to work on metal or wood or any other medium with updates for the address and maybe color.
This is not a for sale sign design request. The sign concept will be used at apartment buildings. Sample property photos are attached - we are looking for a design template that is flexible enough to work on various property types. Also could be wall mounted or a pylon sign. Concept should work either way.

Target Market(s)

Prospective Tenants 25-45 yrs of age with incomes ranging from $55k - $95k.

Industry/Entity Type

Real Estate - Apartments

Colors
59FF00
82FF00
B8FF75
E3FFCB
F4FFEA

Requirements
Must have
• The street address number, web address(www.amberridgeholdingsgroup.com), & incorporate our primary colors(green,white,black)
Nice to have
• "418 Birch St." by Amber Ridge
Should not have
• Should not say For Sale, For Lease, post our phone number.

```html
<!DOCTYPE html>
<html lang="en">
<head>
<meta charset="utf-8">
<title>418 Birch St – Property Sign</title>
<link rel="stylesheet" href="https://fonts.googleapis.com/css2?family=Saira:wght@300;400;700;800&display=swap">
<style>
  :root {
    --backdrop: #e6e6e6;
    --frame: #ffffff;
    --panel: #2a2928;
    --green: #86c440;
    --grey: #a7a9ac;
    --white: #ffffff;
  }
  * { margin: 0; padding: 0; box-sizing: border-box; }
  html, body {
    width: 1076px; height: 1200px; overflow: hidden;
    background: var(--backdrop);
    font-family: "Saira", sans-serif;
  }
  .sign {
    position: absolute; left: 90px; top: 40px;
    width: 896px; height: 1120px;
    background: var(--frame);
    padding: 28px;
  }
  .sign__face {
    width: 840px; height: 1064px;
    display: flex; flex-direction: column;
  }
  .sign__body {
    height: 822px; background: var(--panel);
    position: relative;
  }
  .brand {
    position: absolute; top: 172px; left: 0; right: 0;
    text-align: center; color: var(--green);
    font-weight: 800; text-transform: uppercase; line-height: 1;
  }
  .brand__name { font-size: 76px; letter-spacing: 2px; display: block; }
  .brand__suffix { font-size: 34px; letter-spacing: 5px; display: block; margin-top: 18px; }
  .website {
    position: absolute; top: 560px; left: 0; right: 0;
    text-align: center; font-size: 40px; font-weight: 800;
    color: var(--green); letter-spacing: 1px; line-height: 1;
  }
  .website__tld { color: var(--grey); }
  .sign__address {
    height: 242px; background: var(--green);
    color: var(--white); text-align: center;
    padding-top: 28px;
  }
  .address__street { font-size: 122px; font-weight: 800; line-height: 1; letter-spacing: 1px; }
  .address__tagline { font-size: 44px; font-weight: 400; line-height: 1; margin-top: 20px; }
</style>
</head>
<body>
  <div class="sign">
    <div class="sign__face">
      <div class="sign__body">
        <div class="brand">
          <span class="brand__name">Amber Ridge</span>
          <span class="brand__suffix">Holdings Group LLC</span>
        </div>
        <p class="website">amberridgeholdingsgroup<span class="website__tld">.com</span></p>
      </div>
      <div class="sign__address">
        <p class="address__street">418 Birch St</p>
        <p class="address__tagline">by Amber Ridge Holdings Group</p>
      </div>
    </div>
  </div>
</body>
</html>
```